make it look old timey and motherly but mordern...bath soak with cooling vapors. tall pine hush

need a bath soak label...cooling vapors. will be in a pouch like below. dont pay attention to the design, just attatching so you know the kind of pouch itll be in. need something trusty, minimal and clean...its called tall pine hush bath soak the best bath yull ever take.... for sore muscles, cooling vapors, smells good...made with menthol lemon and eucalyptus...give me something good.

Target Market(s)

make it look old timey and motherly but mordern

Font styles to use
Serif
Sans Serif

Colors
0054AA
0677BA
7BADD7
CADEEF
E8F1F8
0094D4
00A9DD
6FCCEA
C7EBF8
E9F6FB
FFF300
FFF600
FEFA6F
FFFEC7
FFFEE8
FFC000
F8CF3A
FAE287
FDF2CF
FEFAEE
E54698
E96AAD
F1A4CE
F9D9EA
FCEFF6
6B429C
8869AF
B7A5CE
E3DAEB
F3F0F8

```html
<!DOCTYPE html>
<html lang="en">
<head>
<meta charset="utf-8">
<title>Tall Pine Hush Bath Soak – Label</title>
<link rel="stylesheet" href="https://fonts.googleapis.com/css2?family=Italiana&family=Cormorant+Garamond:wght@500&display=swap">
<style>
  :root {
    --backdrop: #efefef;
    --sun-yellow: #fff300;
    --band-yellow: #fff600;
    --pine-green: #5cc88a;
    --sea-teal: #2fb3b0;
    --sky-blue: #0094d4;
    --deep-blue: #0054aa;
    --paper-white: #ffffff;
  }
  * { margin: 0; padding: 0; box-sizing: border-box; }
  html, body {
    width: 1200px;
    height: 835px;
    overflow: hidden;
    background: var(--backdrop);
  }
  .canvas {
    position: relative;
    width: 1200px;
    height: 835px;
  }
  .label {
    position: absolute;
    left: 362px;
    top: 37px;
    width: 476px;
    height: 760px;
    overflow: hidden;
  }
  .label-art {
    position: absolute;
    inset: 0;
  }
  .product-title {
    position: absolute;
    left: 0;
    right: 0;
    top: 118px;
    text-align: center;
    font-family: "Italiana", serif;
    font-size: 80px;
    line-height: 73px;
    color: var(--paper-white);
  }
  .tagline {
    position: absolute;
    left: 0;
    right: 0;
    top: 500px;
    text-align: center;
    font-family: "Italiana", serif;
    font-size: 25px;
    letter-spacing: 0.5px;
    color: var(--paper-white);
  }
  .ingredients {
    position: absolute;
    left: 178px;
    width: 120px;
    top: 570px;
    text-align: center;
    font-family: "Italiana", serif;
    font-size: 15px;
    line-height: 18px;
    color: var(--deep-blue);
  }
  .net-weight {
    position: absolute;
    left: 0;
    right: 0;
    top: 662px;
    text-align: center;
    font-family: "Cormorant Garamond", serif;
    font-weight: 500;
    font-size: 15px;
    line-height: 18px;
    letter-spacing: 0.4px;
    color: var(--paper-white);
  }
</style>
</head>
<body>
<main class="canvas">
  <section class="label">
    <svg class="label-art" width="476" height="760" viewBox="0 0 476 760" aria-hidden="true">
      <defs>
        <linearGradient id="label-fade" x1="0" y1="0" x2="0" y2="1">
          <stop offset="0" stop-color="var(--sun-yellow)"/>
          <stop offset="0.45" stop-color="var(--pine-green)"/>
          <stop offset="0.75" stop-color="var(--sea-teal)"/>
          <stop offset="1" stop-color="var(--sky-blue)"/>
        </linearGradient>
      </defs>
      <rect class="label-ground" width="476" height="760" fill="url(#label-fade)"/>
      <path class="hang-tab" d="M168 0 H307 V34 A69.5 69.5 0 0 1 168 34 Z" fill="var(--paper-white)"/>
      <rect class="label-frame" x="40" y="40" width="396" height="680" fill="none" stroke="var(--band-yellow)" stroke-width="2.5"/>
      <rect class="ingredient-band" x="40" y="557" width="396" height="73" fill="var(--band-yellow)"/>
      <ellipse class="ingredient-seal" cx="238" cy="592" rx="63" ry="46" fill="var(--paper-white)" stroke="var(--band-yellow)" stroke-width="3"/>
    </svg>
    <h1 class="product-title">Tall<br>Pine<br>Hush<br>Bath<br>Soak</h1>
    <p class="tagline">The Best Bath Yull Ever Take</p>
    <p class="ingredients">Made With<br>Menthol , lemon<br>And Eucalyptus</p>
    <p class="net-weight">Net Weight<br>450 gram</p>
  </section>
</main>
</body>
</html>
```